Graniteway Surface Works, Inc. Business Card

New business, we do epoxy, polishing concrete, underlayment, fluid applied flooring, sound proofing, double sided, will need 3 sets of cards with 3 different names and phone numbers.
Company: Graniteway Surface Works, Inc.
Address and Phone: 6339 Charlotte Pike PMB 2183Nashville, TN 38514
(615) 418-3927
www.granitewaysurfaceworks.example

Target Market(s)

General Contractors, Contractors, Architects

Contact Information for Business Card

1st Card: Devon Halvorsen C. 708.214.5873 e. devon@granitewaysurfaceworks.example
Vice President
2nd Card: Morgan Prescoe C. 708.389.6145 e. morgan@granitewaysurfaceworks.example
President
3rd Card: Bo Vu C. 405.631.8207 e. bo@granitewaysurfaceworks.example
Managing Partner

Font styles to use
Serif
Sans Serif

Requirements
Must have
• Professional Clean Design, Implement colors from Logo or nicely contrasting
Nice to have
• N/A

```html
<!DOCTYPE html>
<html lang="en">
<head>
<meta charset="utf-8">
<title>Graniteway Surface Works, Inc. Business Card</title>
<link rel="stylesheet" href="https://fonts.googleapis.com/css2?family=Montserrat:wght@400;500;700&display=swap">
<style>
  :root {
    --page: #ececec;
    --card: #f4f4f5;
    --brand-blue: #0a47a0;
    --brand-green: #3f8a2f;
    --ink: #161616;
    --emboss: #e4e4e6;
  }
  * { margin: 0; padding: 0; box-sizing: border-box; }
  html, body {
    width: 1200px; height: 1200px; overflow: hidden;
    background: var(--page);
    font-family: "Montserrat", sans-serif;
    color: var(--ink);
  }
  .card {
    position: absolute;
    left: 209px;
    width: 796px; height: 441px;
    background: var(--card);
    overflow: hidden;
  }
  .card--front { top: 98px; }
  .card--back { top: 634px; }

  .holder-name {
    position: absolute; left: 50px; top: 40px;
    font-size: 30px; font-weight: 700; color: var(--brand-blue);
    letter-spacing: -0.2px;
  }
  .holder-title {
    position: absolute; left: 50px; top: 75px;
    font-size: 17px; font-weight: 400;
  }
  .address {
    position: absolute; left: 50px; top: 247px;
    font-size: 17px; line-height: 23px; font-weight: 400;
  }
  .contact-list {
    position: absolute; left: 50px; top: 302px;
    list-style: none;
    font-size: 17px; font-weight: 400;
  }
  .contact-list li {
    display: flex; align-items: center;
    height: 25px;
  }
  .contact-icon {
    width: 15px; height: 15px; margin-right: 6px;
    fill: var(--brand-green);
  }
  .emboss-name {
    position: absolute; right: 22px; top: 110px;
    text-align: right;
    font-size: 56px; line-height: 62px; font-weight: 500;
    color: var(--emboss);
    letter-spacing: 1px;
  }
  .emboss-square {
    position: absolute; right: 90px; top: 28px;
    width: 60px; height: 60px;
    background: var(--emboss);
  }

  .brand-lockup {
    position: absolute; left: 0; right: 0; top: 120px;
    display: flex; flex-direction: column; align-items: center;
  }
  .brand-square {
    width: 96px; height: 96px;
    background: var(--brand-blue);
    margin-bottom: 28px;
  }
  .brand-name {
    font-size: 27px; font-weight: 500; color: var(--ink);
    letter-spacing: 1.5px; text-transform: uppercase;
  }
</style>
</head>
<body>

<section class="card card--front">
  <div class="emboss-square"></div>
  <div class="emboss-name">Graniteway<br>Surface<br>Works</div>

  <h1 class="holder-name">Devon Halvorsen</h1>
  <p class="holder-title">Vice President</p>

  <p class="address">4812 Wendover Ridge PMB 7416<br>Nashville, TN 38514</p>

  <ul class="contact-list">
    <li>
      <svg class="contact-icon" viewBox="0 0 16 16" aria-hidden="true"><path d="M4 0h8a1.5 1.5 0 0 1 1.5 1.5v13A1.5 1.5 0 0 1 12 16H4a1.5 1.5 0 0 1-1.5-1.5v-13A1.5 1.5 0 0 1 4 0zm0.3 1.6v11h7.4v-11zM8 13.4a.9.9 0 1 0 0 1.8.9.9 0 0 0 0-1.8z"/></svg>
      708.214.5873
    </li>
    <li>
      <svg class="contact-icon" viewBox="0 0 16 16" aria-hidden="true"><path d="M3.2 1.2l2.2-.4 1.3 3.2-1.5 1.2a8 8 0 0 0 4.6 4.6l1.2-1.5 3.2 1.3-.4 2.2c-.2.9-1 1.5-1.9 1.4C6.4 12.7 2.6 8.9 1.8 3.1c-.1-.9.5-1.7 1.4-1.9zM9 1.5a5.5 5.5 0 0 1 5.5 5.5h-1.3A4.2 4.2 0 0 0 9 2.8zm0 2.6A2.9 2.9 0 0 1 11.9 7h-1.3A1.6 1.6 0 0 0 9 5.4z"/></svg>
      (615) 418-3927
    </li>
    <li>
      <svg class="contact-icon" viewBox="0 0 16 16" aria-hidden="true"><path d="M0 3h16v1.2L8 9 0 4.2zm0 2.6l8 4.8 8-4.8V13H0z"/></svg>
      devon@granitewaysurfaceworks.example
    </li>
    <li>
      <svg class="contact-icon" viewBox="0 0 16 16" aria-hidden="true"><path d="M8 0a8 8 0 1 0 0 16A8 8 0 0 0 8 0zm-1 2.2c-.6.8-1.8 1.1-2 2.2-.2 1 .9 1.4 1.7 1.8.9.5.4 1.7 1.3 2.3.8.5 1.2 1.5.7 2.4-.4.8-.2 2.1-1 2.6A6.4 6.4 0 0 1 7 2.2zm3.2.4a6.4 6.4 0 0 1 3.9 7.3c-.7-.3-1.2-1.1-2-1.1-.9 0-1.4-.8-1.6-1.6-.2-.9.6-1.5.3-2.3-.3-.9-1-1.3-.6-2.3z"/></svg>
      www.granitewaysurfaceworks.example
    </li>
  </ul>
</section>

<section class="card card--back">
  <div class="brand-lockup">
    <div class="brand-square"></div>
    <p class="brand-name">Graniteway Surface Works</p>
  </div>
</section>

</body>
</html>
```